Commercial facility maintenance

I need a card design that helps my salesmen make contact with new clients, our product is facility maintenance and heavy industrial maintenance

```html
<!DOCTYPE html>
<html lang="en">
<head>
<meta charset="utf-8">
<title>Harlow Millwrights – Business Card</title>
<link href="https://fonts.googleapis.com/css2?family=Montserrat:wght@400;500;700&display=swap" rel="stylesheet">
<style>
  :root{
    --stage:#322f38;
    --paper:#f6f6f5;
    --ink:#34363b;
    --brand-red:#8c1c24;
    --steel-dark:#2e3034;
    --steel-mid:#56595f;
  }
  *{box-sizing:border-box;margin:0;padding:0}
  html,body{width:1200px;height:1200px;overflow:hidden;background:var(--stage)}
  body{position:relative;font-family:"Montserrat",sans-serif;color:var(--ink)}
  .card{position:absolute;left:304px;width:618px;height:372px;overflow:hidden}
  .card--front{top:204px;background:var(--paper)}
  .card--back{top:619px;height:381px}

  .wordmark{position:absolute;left:28px;top:38px;display:flex;align-items:center;gap:14px}
  .wordmark__dot{width:70px;height:70px;border-radius:50%;background:var(--ink)}
  .wordmark__name{font-weight:700;font-size:26px;line-height:1.05;color:var(--ink);letter-spacing:.5px}

  .divider{position:absolute;left:0;top:155px;width:410px;height:3px;background:var(--brand-red)}

  .contact{position:absolute;left:34px;top:182px}
  .contact__name{font-weight:700;font-size:19px;color:var(--brand-red);letter-spacing:.6px}
  .contact__role{font-size:17px;margin-top:4px;font-weight:500}
  .contact__list{list-style:none;margin-top:12px}
  .contact__item{display:flex;align-items:flex-start;gap:10px;font-size:15.5px;line-height:22px;margin-bottom:7px;font-weight:500}
  .contact__icon{width:20px;height:20px;flex:none;margin-top:1px;fill:var(--brand-red)}

  .back__surface{position:absolute;inset:0;background:radial-gradient(circle at 50% 45%,var(--steel-mid),var(--steel-dark) 80%)}
  .back__seal{position:absolute;left:148px;top:24px;width:336px;height:336px;border-radius:50%;background:var(--paper);display:flex;align-items:center;justify-content:center;text-align:center}
  .back__seal-name{font-weight:700;font-size:30px;line-height:1.15;color:var(--ink);letter-spacing:1px}
</style>
</head>
<body>
  <section class="card card--front">
    <div class="wordmark">
      <span class="wordmark__dot"></span>
      <span class="wordmark__name">HARLOW<br>MILLWRIGHTS LLC.</span>
    </div>
    <div class="divider"></div>
    <div class="contact">
      <p class="contact__name">DANIEL HARLOW</p>
      <p class="contact__role">Owner / Millwright</p>
      <ul class="contact__list">
        <li class="contact__item">
          <svg class="contact__icon" viewBox="0 0 24 24"><path d="M6.6 10.8a15.1 15.1 0 0 0 6.6 6.6l2.2-2.2a1 1 0 0 1 1-.25 11.4 11.4 0 0 0 3.6.6 1 1 0 0 1 1 1V20a1 1 0 0 1-1 1A17 17 0 0 1 3 4a1 1 0 0 1 1-1h3.5a1 1 0 0 1 1 1c0 1.25.2 2.45.6 3.6a1 1 0 0 1-.25 1z"/></svg>
          <span>(555) 201-3846</span>
        </li>
        <li class="contact__item">
          <svg class="contact__icon" viewBox="0 0 24 24"><path d="M2 5h20v14H2z M2 5l10 8 10-8" /><path d="M2 6.5l10 7.5 10-7.5V5H2z" fill="#f6f6f5"/></svg>
          <span>daniel@harlowmillwrights.com</span>
        </li>
        <li class="contact__item">
          <svg class="contact__icon" viewBox="0 0 24 24"><path d="M12 2a7 7 0 0 0-7 7c0 5.2 7 13 7 13s7-7.8 7-13a7 7 0 0 0-7-7zm0 9.5A2.5 2.5 0 1 1 12 6.5a2.5 2.5 0 0 1 0 5z"/></svg>
          <span>88 Foundry Ave.<br>Riverton, USA 40512</span>
        </li>
      </ul>
    </div>
  </section>

  <section class="card card--back">
    <div class="back__surface" role="img" aria-label="Scratched brushed steel texture background"></div>
    <div class="back__seal">
      <p class="back__seal-name">HARLOW<br>MILLWRIGHTS<br>LLC</p>
    </div>
  </section>
</body>
</html>
```